Cover Art Needed For Digital Single Release

We are looking to have the cover art designed for a new song called "Paper Lanterns". You will find the track attached below in a private Tunepool link so that you can have a listen.
We are thinking of keeping the artwork fairly simple but still want it to catch your eye. Maybe using the song title and artist’s name in a colorful and creative way. (A well-designed font with a bold color scheme, or even something like a mosaic style art piece featuring the title).
We completely welcome any and all creative visions you might have, even if it strays away from the examples given above.
Thank you in advance for your submissions, and we are excited to collaborate with you!
"Paper Lanterns" by Marcus Fell
https://tunepool.example/marcuszxq/paper-lanterns/s-r7tWnexiLqa
Target Market(s)
Teens/Young Adults
Industry/Entity Type
Music
Requirements
Must have
- An eye-catching design
Should not have
- Please do not rely heavily on stock images. We prefer an original design/concept.

```html
<!DOCTYPE html>
<html lang="en">
<head>
<meta charset="utf-8">
<title>Paper Lanterns — Marcus Fell</title>
<link href="https://fonts.googleapis.com/css2?family=Bebas+Neue&family=Josefin+Sans:wght@400&display=swap" rel="stylesheet">
<style>
  :root {
    --paper: #ffffff;
    --lemon: #f2ea22;
    --magenta: #bf61a5;
    --cyan: #66cbe0;
    --blush: #f4abcb;
    --white: #ffffff;
  }
  html, body {
    margin: 0;
    padding: 0;
    width: 1200px;
    height: 1000px;
    overflow: hidden;
    background: var(--paper);
  }
  .cover {
    display: block;
    width: 1200px;
    height: 1000px;
  }
  .cover__field { fill: var(--lemon); }
  .cover__title {
    font-family: "Bebas Neue", "Oswald", sans-serif;
    mix-blend-mode: multiply;
  }
  .cover__title--top { fill: var(--magenta); }
  .cover__title--bottom { fill: var(--cyan); }
  .cover__artist {
    font-family: "Josefin Sans", "Montserrat", sans-serif;
    font-size: 31px;
    fill: var(--white);
  }
</style>
</head>
<body>
<svg class="cover" viewBox="0 0 1200 1000" xmlns="http://www.w3.org/2000/svg">
  <defs>
    <linearGradient id="figure-tone" x1="0" y1="0" x2="0" y2="1">
      <stop offset="0" stop-color="#f7d64a"/>
      <stop offset="0.45" stop-color="#f4abcb"/>
      <stop offset="1" stop-color="#ffffff"/>
    </linearGradient>
  </defs>

  <rect class="cover__field" x="209" y="102" width="796" height="796"/>

  <g class="cover__titles" style="isolation:isolate">
    <text class="cover__title cover__title--top" x="253" y="674" font-size="767" textLength="711" lengthAdjust="spacingAndGlyphs">PAPER</text>
    <text class="cover__title cover__title--bottom" x="253" y="863" font-size="771" textLength="711" lengthAdjust="spacingAndGlyphs">LANTERNS</text>
  </g>

  <rect class="cover__figure" role="img" aria-label="Silhouette of a leaping figure in white, pink and yellow tones"
        x="378" y="252" width="306" height="536" rx="120" fill="url(#figure-tone)" opacity="0.7"/>

  <text class="cover__artist" x="342" y="507" textLength="524" lengthAdjust="spacing">MARCUS FELL</text>
</svg>
</body>
</html>
```